Derek Hollins Business card

Hey there, I’m hoping to have a business card designed. I’m in Real estate and just switched to a new Brokerage called: The Property Quarter

The back could just be the company name maybe or whatever looks good!

I’ve attached some logos of our company and some cards my buddy had done up.

On the card:
Derek Hollins
derekhollins@mailbox-demo.com
587-214-6093
derekhollins-demo.ca

Target Market(s)

Home buyers and sellers

Industry/Entity Type

Real Estate

Contact Information for Business Card

just looking for a cool and modern design with my picture on it. I like the idea of Black and red being used.

Requirements
Must have
• all the details provided. I'm open to anything. Just want a professional looking card.

```html
<!DOCTYPE html>
<html lang="en">
<head>
<meta charset="utf-8">
<title>Derek Hollins – Business Card</title>
<link rel="stylesheet" href="https://fonts.googleapis.com/css2?family=Cinzel:wght@400&family=Montserrat:wght@500;800&display=swap">
<style>
  :root {
    --stage: #8c8c8c;
    --card-front: #231f20;
    --card-back: #050607;
    --red: #951b1e;
    --white: #ffffff;
    --rule: #0b0b0b;
    --mark-grey: #4a4a4a;
    --icon-grey: #bdbdbd;
  }
  * { margin: 0; padding: 0; box-sizing: border-box; }
  html, body {
    width: 1200px; height: 1200px; overflow: hidden;
    background: var(--stage);
  }
  .card {
    position: absolute;
    left: 115px;
    width: 970px;
    height: 554px;
    overflow: hidden;
  }
  .card--front { top: 30px; background: var(--card-front); }
  .card--back  { top: 616px; background: var(--card-back); }

  .name-tab {
    position: absolute; left: 0; top: 323px;
    width: 53px; height: 42px; background: var(--red);
  }
  .agent-name {
    position: absolute; left: 76px; top: 318px;
    font-family: "Cinzel", serif; font-size: 44px; line-height: 1;
    letter-spacing: 0.5px; color: var(--white); white-space: nowrap;
  }
  .agent-name .surname { color: var(--red); }
  .name-rule {
    position: absolute; left: 455px; top: 360px;
    width: 515px; height: 2px; background: var(--rule);
  }
  .monogram-name {
    position: absolute; right: 26px; top: 300px;
    font-family: "Cinzel", serif; font-size: 30px; line-height: 1;
    color: var(--mark-grey); white-space: nowrap;
  }

  .contact-list {
    position: absolute; left: 76px; top: 410px;
    list-style: none;
    font-family: "Montserrat", sans-serif; font-weight: 500;
    font-size: 25px; color: var(--white);
  }
  .contact-list li {
    display: flex; align-items: center; gap: 12px;
    height: 32px; white-space: nowrap;
  }
  .contact-list svg { width: 24px; height: 24px; flex: none; }

  .brand {
    position: absolute; left: 90px; top: 112px;
    display: flex; align-items: center; gap: 22px;
  }
  .brand-square { width: 46px; height: 46px; background: var(--red); }
  .brand-name {
    font-family: "Montserrat", sans-serif; font-weight: 800;
    font-size: 62px; line-height: 1.02; letter-spacing: -1px;
    color: var(--white); text-transform: uppercase;
  }
</style>
</head>
<body>
  <section class="card card--front">
    <div class="name-tab"></div>
    <h1 class="agent-name">Derek <span class="surname">Hollins</span></h1>
    <div class="name-rule"></div>
    <div class="monogram-name">Derek Hollins</div>

    <ul class="contact-list">
      <li>
        <svg viewBox="0 0 24 24" fill="none" stroke="var(--icon-grey)" stroke-width="1.5" aria-hidden="true">
          <circle cx="12" cy="12" r="10"/><ellipse cx="12" cy="12" rx="4.5" ry="10"/>
          <line x1="2" y1="12" x2="22" y2="12"/><line x1="4" y1="7" x2="20" y2="7"/><line x1="4" y1="17" x2="20" y2="17"/>
        </svg>
        <span>derekhollins@mailbox-demo.com</span>
      </li>
      <li>
        <svg viewBox="0 0 24 24" fill="none" stroke="var(--icon-grey)" stroke-width="1.5" aria-hidden="true">
          <circle cx="12" cy="12" r="10"/>
          <path d="M8.5 7.5c-.8.8-.6 2.6 1.2 4.8s3.8 3.4 4.9 2.6l1-1-1.8-1.6-1 .8c-.9-.4-2-1.6-2.4-2.4l.8-1-1.6-1.8z"/>
        </svg>
        <span>587-214-6093</span>
      </li>
      <li>
        <svg viewBox="0 0 24 24" fill="none" stroke="var(--icon-grey)" stroke-width="1.5" aria-hidden="true">
          <rect x="2" y="5" width="20" height="14"/><path d="M2 5l10 8 10-8M2 19l7-7M22 19l-7-7"/>
        </svg>
        <span>derekhollins-demo.ca</span>
      </li>
    </ul>
  </section>

  <section class="card card--back">
    <div class="brand">
      <div class="brand-square"></div>
      <div class="brand-name">The Property<br>Quarter</div>
    </div>
  </section>
</body>
</html>
```